Business Card Re-design

We are looking for a fresh bold look for general office business cards. We are a staffing agency that staffs industrial, coal mining, and clerical jobs.
Tag Line: We match the BEST people to the BEST roles.
Marlow Falls Office: 2473 W. Tallow Creek Rd, Marlow Falls, KS - 47308
p. 555.203.6180 f. 555.203.6195
Ashford Office: 264 S. Birch Ln, Ashford, KS - 47152
p. 555.319.2047 f. 555.203.6195
Absentee/Emergency 24hr Hotline 555.203.6172 opt.1
www.bluelanternworkforce.example

```html
<!DOCTYPE html>
<html lang="en">
<head>
<meta charset="utf-8">
<title>Blue Lantern Workforce – Business Cards</title>
<link href="https://fonts.googleapis.com/css2?family=Montserrat:wght@400;500;700&display=swap" rel="stylesheet">
<style>
  :root{
    --backdrop:#2e3032;
    --mint:#5fc38d;
    --navy:#10103d;
    --green:#3a9d4a;
    --white:#ffffff;
  }
  *{box-sizing:border-box;margin:0;padding:0}
  html,body{width:1200px;height:1200px;overflow:hidden}
  body{
    background:radial-gradient(circle at 50% 35%,#4a4c4e 0%,var(--backdrop) 70%);
    font-family:"Montserrat",sans-serif;
    position:relative;
  }
  .card{
    position:absolute;left:180px;width:840px;height:480px;
    box-shadow:0 14px 30px rgba(0,0,0,.45);
    overflow:hidden;
  }
  .card-front{top:60px;background:var(--mint);color:var(--white);border-bottom:8px solid var(--green)}
  .card-back{top:620px;background:var(--navy);color:var(--white)}
  .card-back .accent-band{position:absolute;left:0;right:0;bottom:0;height:12px;background:var(--green)}

  .brand{display:flex;align-items:center;gap:16px;font-weight:700;text-transform:uppercase;letter-spacing:2px;white-space:nowrap}
  .brand-square{width:30px;height:30px;flex:none}

  .front-content{position:absolute;inset:0;display:flex;flex-direction:column;align-items:center;justify-content:center;text-align:center;padding:0 40px}
  .front-content .brand{font-size:40px;color:var(--white)}
  .front-content .brand-square{background:var(--white)}
  .tagline{font-size:17px;margin-top:20px;letter-spacing:.5px}
  .web{font-size:22px;margin-top:44px}
  .hotline{font-size:22px;margin-top:12px}

  .person{position:absolute;right:60px;top:50px;text-align:left}
  .person-name{font-size:30px;color:var(--green);font-weight:400}
  .person-title{font-size:20px;margin-top:6px;margin-left:24px}

  .card-back .brand{position:absolute;left:60px;top:150px;font-size:36px;color:var(--green)}
  .card-back .brand-square{background:var(--green)}

  .office{position:absolute;font-size:19px;line-height:1.45}
  .office-left{left:60px;bottom:52px}
  .office-right{right:60px;bottom:80px;text-align:right}
  .contact-row{display:flex;align-items:center;gap:12px;margin-top:4px}
  .office-right .contact-row{justify-content:flex-end}
  .icon{width:24px;height:24px;fill:var(--green);flex:none}
</style>
</head>
<body>

<section class="card card-front" aria-label="Card front">
  <div class="front-content">
    <div class="brand"><span class="brand-square"></span>Blue Lantern Workforce</div>
    <p class="tagline">We match the BEST people to the BEST roles</p>
    <p class="web">www.bluelanternworkforce.example</p>
    <p class="hotline">Hotline 555.203.6172</p>
  </div>
</section>

<section class="card card-back" aria-label="Card back">
  <div class="person">
    <p class="person-name">Marcus Ellery</p>
    <p class="person-title">CEO</p>
  </div>

  <div class="brand"><span class="brand-square"></span>Blue Lantern Workforce</div>

  <div class="office office-left">
    <p>2473 W. Tallow Creek Rd, Marlow Falls,</p>
    <p>KS - 47308</p>
    <div class="contact-row">
      <svg class="icon" viewBox="0 0 24 24" aria-hidden="true"><path d="M6.6 10.8a15.1 15.1 0 0 0 6.6 6.6l2.2-2.2c.3-.3.7-.4 1-.2 1.1.4 2.3.6 3.6.6.6 0 1 .4 1 1V20c0 .6-.4 1-1 1A17 17 0 0 1 3 4c0-.6.4-1 1-1h3.5c.6 0 1 .4 1 1 0 1.3.2 2.5.6 3.6.1.3 0 .7-.2 1z"/></svg>
      <span>555.203.6180</span>
    </div>
    <div class="contact-row">
      <svg class="icon" viewBox="0 0 24 24" aria-hidden="true"><path d="M6 2h12v6H6zM3 9h18a2 2 0 0 1 2 2v6h-4v5H5v-5H1v-6a2 2 0 0 1 2-2zm4 8v3h10v-3z"/></svg>
      <span>555.203.6195</span>
    </div>
  </div>

  <div class="office office-right">
    <p>264 S. Birch Ln, Ashford,</p>
    <p>KS - 47152</p>
    <div class="contact-row">
      <span>555.203.6180</span>
      <svg class="icon" viewBox="0 0 24 24" aria-hidden="true"><path d="M6.6 10.8a15.1 15.1 0 0 0 6.6 6.6l2.2-2.2c.3-.3.7-.4 1-.2 1.1.4 2.3.6 3.6.6.6 0 1 .4 1 1V20c0 .6-.4 1-1 1A17 17 0 0 1 3 4c0-.6.4-1 1-1h3.5c.6 0 1 .4 1 1 0 1.3.2 2.5.6 3.6.1.3 0 .7-.2 1z"/></svg>
    </div>
    <div class="contact-row">
      <span>555.203.6195</span>
      <svg class="icon" viewBox="0 0 24 24" aria-hidden="true"><path d="M6 2h12v6H6zM3 9h18a2 2 0 0 1 2 2v6h-4v5H5v-5H1v-6a2 2 0 0 1 2-2zm4 8v3h10v-3z"/></svg>
    </div>
  </div>

  <div class="accent-band"></div>
</section>

</body>
</html>
```